Real Estate Business Folders, Business Cards, Envelopes & Letterhead

Im looking for trendy, modern & professional design concepts for my business folder that will be used for real estate documents and property report presentations. I'm also looking for Business card designs, envelopes and letterhead with a similar theme. I have a logo already and I would like the logo colors to be incorporated in the design concepts.

Target Market(s)

Real Estate Investors, Banks, Financial Institutions

Industry/Entity Type

Real Estate

Colors
0455a3
959595
d3d3d3
848484

Requirements
Must have
• Trendy Modern, High Class look. Please include logo and colors and incorporate some silver or metallic.
• Business Address: 4812 Corvelle Blvd ste 210-300
• N. Las Vegas, NV 89084
• Phone: 702-555-0147
• Fax : 702-555-0183
• Email: info@mesacrestlandgroup.example
• Website: MesaCrestLandGroup.example

```html
<!DOCTYPE html>
<html lang="en">
<head>
<meta charset="utf-8">
<title>Mesa Crest Land Group – Business Card</title>
<link rel="stylesheet" href="https://fonts.googleapis.com/css2?family=Cinzel:wght@600&family=Tinos:wght@400&display=swap">
<style>
  :root {
    --brand-blue: #0455a3;
    --silver: #959595;
    --text-grey: #555555;
    --card-white: #ffffff;
    --backdrop: #2b2b2b;
  }
  * { margin: 0; padding: 0; box-sizing: border-box; }
  html, body {
    width: 1125px; height: 1200px; overflow: hidden;
    background: var(--backdrop);
  }
  .canvas { position: relative; width: 1125px; height: 1200px; }
  .card {
    position: absolute; left: 171px; width: 826px; height: 472px;
    background: var(--card-white);
  }
  .card--front { top: 106px; }
  .card--back { top: 639px; }

  .identity {
    position: absolute; right: 492px; top: 206px; text-align: right;
  }
  .identity__name {
    font-family: "Cinzel", "Times New Roman", serif; font-weight: 600;
    font-size: 31px; line-height: 1; color: var(--brand-blue); letter-spacing: 0.5px;
  }
  .identity__title {
    font-family: "Cinzel", "Times New Roman", serif; font-weight: 600;
    font-size: 20px; line-height: 1; color: var(--silver); margin-top: 5px; letter-spacing: 0.5px;
  }
  .divider {
    position: absolute; left: 361px; top: 176px; width: 1px; height: 118px;
    background: var(--silver);
  }
  .contacts {
    position: absolute; left: 390px; top: 178px; list-style: none;
    font-family: "Tinos", "Times New Roman", serif; font-size: 19.5px;
    color: var(--text-grey);
  }
  .contacts li { display: flex; align-items: center; height: 26.5px; }
  .contacts svg { width: 20px; height: 20px; margin-right: 11px; fill: var(--brand-blue); flex: none; }
  .address-band {
    position: absolute; left: 0; top: 394px; width: 100%; height: 40px;
    background: var(--brand-blue); color: var(--card-white);
    font-family: "Tinos", "Times New Roman", serif; font-size: 19.5px;
    display: flex; align-items: center; justify-content: center;
  }

  .wordmark {
    position: absolute; left: 0; top: 0; width: 100%; height: 100%;
    display: flex; align-items: center; justify-content: center; gap: 14px;
  }
  .wordmark__mark { width: 26px; height: 26px; background: var(--brand-blue); }
  .wordmark__name {
    font-family: "Tinos", "Times New Roman", serif; font-weight: 400;
    font-size: 40px; line-height: 1; color: var(--brand-blue);
  }
</style>
</head>
<body>
<main class="canvas">
  <section class="card card--front" aria-label="Business card front">
    <div class="identity">
      <p class="identity__name">DANIEL REYES</p>
      <p class="identity__title">CEO/FOUNDER</p>
    </div>
    <div class="divider"></div>
    <ul class="contacts">
      <li>
        <svg viewBox="0 0 24 24" aria-hidden="true"><path d="M6.6 10.8a15.2 15.2 0 0 0 6.6 6.6l2.2-2.2c.3-.3.7-.4 1-.2 1.1.4 2.3.6 3.6.6.6 0 1 .4 1 1V20c0 .6-.4 1-1 1A17 17 0 0 1 3 4c0-.6.4-1 1-1h3.5c.6 0 1 .4 1 1 0 1.3.2 2.5.6 3.6.1.3 0 .7-.2 1z"/></svg>
        702-555-0147
      </li>
      <li>
        <svg viewBox="0 0 24 24" aria-hidden="true"><path d="M7 2h10v6H7z M3 9h18a1 1 0 0 1 1 1v8h-4v-3H6v3H2v-8a1 1 0 0 1 1-1z M6 16h12v6H6z"/></svg>
        702-555-0183
      </li>
      <li>
        <svg viewBox="0 0 24 24" aria-hidden="true"><path d="M2 6h20v13H2z M2.5 6.5 12 13l9.5-6.5" fill="none" stroke="#0455a3" stroke-width="2"/></svg>
        info@mesacrestlandgroup.example
      </li>
      <li>
        <svg viewBox="0 0 24 24" aria-hidden="true"><circle cx="12" cy="12" r="10"/><path d="M7 6c2 1 3 3 2 5s1 3 3 3 1 3 0 5M14 4c0 2 2 3 4 3" fill="none" stroke="#fff" stroke-width="1.6"/></svg>
        www.MesaCrestLandGroup.example
      </li>
    </ul>
    <div class="address-band">4812 Corvelle Blvd ste 210-300, N. Las Vegas, NV 89084</div>
  </section>

  <section class="card card--back" aria-label="Business card back">
    <div class="wordmark">
      <span class="wordmark__mark" aria-hidden="true"></span>
      <span class="wordmark__name">Mesa Crest Land Group</span>
    </div>
  </section>
</main>
</body>
</html>
```